Thank You For Shopping / Hair Care Tips

I need “Thank You For Shopping”
Post cards made for my hair business !
I added pictures of post cards that I really like . I also added my LuzeKora Wigs logo for you guys to use

I want the backside of the flyer to have hair care tips !
I want people to have full directions on how to care for their wigs

Target Market(s)

Im marking to young woman to older middle aged woman
Ages 23-66 . I want my flyer to look mature And classy

Industry/Entity Type

Hair And Beauty

Font styles to use
Serif
Script

Colors
e34699
e34298
e34398

Requirements
Must have
• The flyer must have the Instagram logo with my Instagram name next to it @luze.kora.wigs__
• Also it must have my “Luze Kora Wigs” logo that I’ve uploaded in the pictures section .
• Flyer had to be two sides . One side “ thank you for shopping “ side two “hair care tips”
• My website must be on the flyer - www.luzekorawigs.example
• The flyer must match the colors of my logo
• All white . With the pink and glitter sliver you see on my logo
Nice to have
• Nice to have a glitter border
Should not have
• The flyer should not have different colors that don’t match my logo
• It shouldn’t be made without having my Instagram or website on the flyer

```html
<!DOCTYPE html>
<html lang="en">
<head>
<meta charset="utf-8">
<title>LuzeKora Wigs – Thank You &amp; Hair Care Tips Cards</title>
<link href="https://fonts.googleapis.com/css2?family=Great+Vibes&family=Yellowtail&family=Montserrat:wght@400;500;700&display=swap" rel="stylesheet">
<style>
  :root{
    --pink:#e34398;
    --silver-light:#e6e6e6;
    --silver-mid:#bdbdbd;
    --silver-dark:#9a9a9a;
    --grey-text:#6f6f6f;
    --body-text:#3a3a3a;
    --card:#ffffff;
    --backdrop:#e4e4e4;
  }
  *{box-sizing:border-box;margin:0;padding:0}
  html,body{width:714px;height:1200px;overflow:hidden}
  body{background:var(--backdrop);font-family:'Montserrat',sans-serif;position:relative}

  .card{position:absolute;left:47px;width:620px;height:411px;background:var(--card);
        box-shadow:0 6px 12px rgba(0,0,0,.28)}
  .card--thanks{top:166px}
  .card--tips{top:622px}

  /* glitter frame */
  .glitter-frame{position:absolute;inset:0;border:13px solid var(--silver-mid);
        border-image:linear-gradient(135deg,var(--silver-light),var(--silver-dark) 30%,var(--silver-light) 55%,var(--silver-dark) 80%,var(--silver-light)) 1;}

  .thanks-title{position:absolute;top:42px;left:0;width:100%;text-align:center;
        font-family:'Yellowtail',cursive;font-size:104px;line-height:1;color:var(--pink)}
  .shopping-band{position:absolute;top:176px;left:70px;right:70px;height:74px;
        background:linear-gradient(#f5f5f5,#fff 18%,#fff 82%,#f7f7f7);}
  .shopping-label{position:absolute;top:186px;left:0;width:100%;text-align:center;
        font-weight:700;font-size:40px;letter-spacing:2px;color:var(--silver-dark)}

  .brand-name{position:absolute;font-family:'Montserrat',sans-serif;font-weight:700;color:var(--grey-text)}
  .card--thanks .brand-name{left:70px;top:298px;width:200px;text-align:center;font-size:26px;line-height:1.15}
  .divider{position:absolute;left:286px;top:266px;width:1px;height:100px;background:#d5d5d5}

  .contact{position:absolute;left:314px;display:flex;align-items:center;gap:14px;
        font-size:17px;color:var(--body-text);letter-spacing:.5px}
  .contact--social{top:294px}
  .contact--web{top:341px}
  .social-mark{width:24px;height:24px;border:2.5px solid var(--pink);border-radius:5px}

  .tips-corner{position:absolute;inset:0}
  .tips-title{position:absolute;top:30px;left:0;width:100%;text-align:center;
        font-family:'Great Vibes',cursive;font-size:80px;line-height:1;color:var(--pink)}
  .tips-intro{position:absolute;top:140px;left:56px;right:56px;text-align:center;
        font-size:11.2px;line-height:1.3;color:var(--body-text)}
  .tips-list{position:absolute;top:196px;left:52px;right:52px;list-style:none;
        display:grid;grid-template-columns:1fr 1fr;column-gap:34px;row-gap:11px}
  .tips-list li{display:flex;gap:9px;font-size:10.8px;line-height:1.22;color:var(--body-text)}
  .tick{flex:none;width:10px;height:10px;margin-top:1px}
  .card--tips .brand-name{left:0;width:100%;top:313px;text-align:center;font-size:20px;line-height:1.15}
  .tips-url{position:absolute;top:380px;left:0;width:100%;text-align:center;
        font-size:9.5px;letter-spacing:4.5px;color:var(--body-text)}
</style>
</head>
<body>

<section class="card card--thanks">
  <div class="glitter-frame"></div>
  <h1 class="thanks-title">Thank You</h1>
  <div class="shopping-band"></div>
  <p class="shopping-label">FOR SHOPPING</p>
  <p class="brand-name">LuzeKora<br>Wigs</p>
  <div class="divider"></div>
  <p class="contact contact--social"><span class="social-mark"></span>@luze.kora.wigs__</p>
  <p class="contact contact--web">
    <svg width="26" height="26" viewBox="0 0 26 26" fill="none" stroke="var(--pink)" stroke-width="1.3">
      <circle cx="13" cy="13" r="11"/><ellipse cx="13" cy="13" rx="5" ry="11"/>
      <line x1="2" y1="13" x2="24" y2="13"/><line x1="4" y1="7.5" x2="22" y2="7.5"/><line x1="4" y1="18.5" x2="22" y2="18.5"/>
    </svg>
    www.luzekorawigs.example
  </p>
</section>

<section class="card card--tips">
  <svg class="tips-corner" width="620" height="411" viewBox="0 0 620 411">
    <polygon fill="var(--pink)" points="418,0 620,0 620,195 607,178 607,13 431,13"/>
    <polygon fill="var(--pink)" points="0,228 13,245 13,398 182,398 195,411 0,411"/>
  </svg>
  <h2 class="tips-title">Hair Care Tips</h2>
  <p class="tips-intro">Lorem ipsum dolor sit amet, consectetur adipiscing elit, sed do eiusmod tempor incidi-<br>dunt ut labore et dolore magna aliqua. Ut enim ad minim veniam.</p>
  <ul class="tips-list">
    <li><svg class="tick" viewBox="0 0 10 10"><path d="M1 5.5l2.6 2.6L9 2" fill="none" stroke="var(--pink)" stroke-width="2"/></svg>Lorem ipsum dolor sit amet,consectetur adipiscing elit.</li>
    <li><svg class="tick" viewBox="0 0 10 10"><path d="M1 5.5l2.6 2.6L9 2" fill="none" stroke="var(--pink)" stroke-width="2"/></svg>Lorem ipsum dolor sit amet, consectetur adipiscing elit.</li>
    <li><svg class="tick" viewBox="0 0 10 10"><path d="M1 5.5l2.6 2.6L9 2" fill="none" stroke="var(--pink)" stroke-width="2"/></svg>Lorem ipsum dolor sit amet, consectetur adipiscing elit.</li>
    <li><svg class="tick" viewBox="0 0 10 10"><path d="M1 5.5l2.6 2.6L9 2" fill="none" stroke="var(--pink)" stroke-width="2"/></svg>Lorem ipsum dolor sit amet, consectetur adipiscing elit.</li>
    <li><svg class="tick" viewBox="0 0 10 10"><path d="M1 5.5l2.6 2.6L9 2" fill="none" stroke="var(--pink)" stroke-width="2"/></svg>Lorem ipsum dolor sit amet, consectetur adipiscing elit.</li>
    <li><svg class="tick" viewBox="0 0 10 10"><path d="M1 5.5l2.6 2.6L9 2" fill="none" stroke="var(--pink)" stroke-width="2"/></svg>Lorem ipsum dolor sit amet, consectetur adipiscing elit.</li>
  </ul>
  <p class="brand-name">LuzeKora<br>Wigs</p>
  <p class="tips-url">www.luzekorawigs.example</p>
</section>

</body>
</html>
```